Capability Statement Document/Flyer

Take the existing words from the capability statement document (attached) and design a unique folder/flyer document for professional use. Maybe something like a trifold or bifold style. Use approved colours and logo as per the attached files.
Our company designs and builds small onshore gas processing plants.

```html
<!DOCTYPE html>
<html lang="en">
<head>
<meta charset="utf-8">
<title>Vantaflo Capability Statement</title>
<link href="https://fonts.googleapis.com/css2?family=Poppins:ital,wght@0,400;0,500;0,600;0,700;1,600;1,700&display=swap" rel="stylesheet">
<style>
:root{
  --green:#0f7360;
  --green-dark:#0a5546;
  --green-deep:#083f35;
  --teal:#1ea58c;
  --ink:#1d1d1d;
  --grey:#9c9c9c;
  --grey-light:#e9eaec;
  --bg:#f1f1f1;
  --white:#ffffff;
}
*{box-sizing:border-box;margin:0;padding:0}
html,body{width:1025px;height:1200px;overflow:hidden;background:var(--bg);font-family:"Poppins",sans-serif;color:var(--ink)}
.sheet-grid{position:absolute;left:27px;top:150px;display:grid;grid-template-columns:repeat(3,310px);grid-template-rows:repeat(2,437px);gap:26px 22px}
.page{position:relative;width:310px;height:437px;background:var(--white);overflow:hidden;box-shadow:0 3px 8px rgba(0,0,0,.28)}
.abs{position:absolute}
.photo{position:absolute}
.corner{position:absolute;right:0;bottom:0}

/* cover */
.cover-top{left:0;top:0;width:310px;height:58px;background:#f6f6f7;display:flex;align-items:center;justify-content:center}
.brand{font-weight:600;color:var(--green);letter-spacing:.5px}
.cover-top .brand{font-size:22px}
.cover-photo{left:0;top:58px;width:310px;height:273px;background:linear-gradient(180deg,#2a2c36 0%,#5c616b 40%,#9ea3aa 75%,#7c8088 100%)}
.cover-band{left:0;top:331px;width:310px;height:106px;background:var(--green);text-align:center;color:var(--white)}
.cover-title{margin-top:14px;font-size:18px;font-weight:700;color:#d9e2df;letter-spacing:.5px}
.cover-sub{margin-top:5px;font-size:10.5px;line-height:1.5;font-weight:500}
.cover-url{margin-top:10px;font-size:6px;font-weight:600}

/* intro page */
.intro-photo{left:0;top:0;width:310px;height:176px;background:linear-gradient(160deg,#7fa8c8 0%,#c7d3da 35%,#9a948a 65%,#b59b76 100%);clip-path:polygon(0 0,100% 0,100% 100%,0 100%)}
.h-green{color:var(--green);font-weight:700;text-transform:uppercase}
.intro-h{left:19px;top:188px;width:150px;font-size:8px;line-height:1.25}
.body{font-size:5.1px;line-height:1.5;color:#222}
.intro-p{left:19px;top:214px;width:150px}
.principles-h{left:19px;top:272px;font-size:7px;font-weight:700;font-style:italic;color:var(--green)}
.principles{left:25px;top:283px;list-style:none}
.principles li{font-size:5px;line-height:1.9}
.obj-h{left:19px;top:337px;font-size:7px;font-weight:700;color:var(--green)}
.obj-p{left:19px;top:350px;width:84px}
.who-box{left:181px;top:174px;width:114px;height:121px;background:var(--green);border:2px solid var(--white);outline:1px solid var(--green);color:var(--white);text-align:center;padding:8px 6px}
.who-box h3{font-size:7.5px;font-weight:700;margin-bottom:5px}
.who-box p{font-size:4.8px;line-height:1.35;color:#cfe9df}
.who-box .vision{margin-top:8px;font-size:5px;font-weight:700;font-style:italic;color:var(--white)}
.diag-row{position:absolute;left:119px;width:168px;height:19px;background:var(--grey-light);border-radius:2px}
.diag-label{position:absolute;left:14px;top:0;width:60px;height:19px;display:flex;align-items:center;justify-content:center;text-align:center;font-size:5.3px;font-weight:600;color:var(--green);line-height:1.1}
.chip{position:absolute;top:2px;height:15px;width:26px;background:var(--green);border:1px solid #9fd4c4;color:var(--white);font-size:3.6px;display:flex;align-items:center;justify-content:center;text-align:center;line-height:1.1;border-radius:1px}

/* services page */
.slant{left:0;top:0}
.svc-title{right:26px;top:22px;font-size:7.5px;font-weight:700;color:var(--green)}
table{border-collapse:collapse}
.svc-table{position:absolute;left:13px;top:47px;width:284px}
.svc-table th{background:var(--green);color:var(--white);font-size:6.4px;font-weight:700;height:23px;text-align:left;padding-left:4px;border:1px solid var(--white)}
.svc-table th.c{text-align:center}
.svc-table th.num{background:#9aa6a2;text-align:center}
.svc-table td{font-size:4.5px;height:13.5px;border:.6px solid var(--green);padding:0 3px;line-height:1.15}
.svc-table td.num{text-align:center;width:20px}
.svc-table td.fn{color:var(--green);font-weight:600;width:85px}
.roles-title{left:0;width:310px;top:275px;text-align:center;font-size:7.5px;font-weight:700;color:var(--green)}
.roles-table{position:absolute;left:41px;top:292px;width:227px}
.roles-table th{background:var(--green);color:var(--white);font-size:6.2px;font-weight:700;height:23px;text-align:left;padding-left:6px;border:1px solid var(--white)}
.roles-table td{font-size:4.7px;height:13.3px;border:.6px solid var(--green);padding:0 6px}

/* benefits page */
.ben-bg{left:0;top:0;width:310px;height:300px;background:linear-gradient(180deg,#4f8e81 0%,#2f7868 50%,#6f9d93 100%)}
.ben-panel{left:14px;top:0;width:156px;height:176px;background:var(--green-dark);clip-path:polygon(0 0,100% 0,100% 100%,0 100%)}
.chal-panel{left:14px;top:163px;width:156px;height:137px;background:#0b2923;clip-path:polygon(0 14%,100% 0,100% 100%,0 100%)}
.panel-h{font-size:7px;font-weight:600;color:var(--white);line-height:1.3}
.bullets{list-style:none}
.bullets li{position:relative;padding-left:6px;color:#e7f2ee}
.bullets li::before{content:"•";position:absolute;left:0}
.ben-list li{font-size:5px;line-height:1.25;margin-bottom:5px}
.chal-list li{font-size:4.5px;line-height:1.25;margin-bottom:3px}
.ben-art{left:0;top:300px;width:310px;height:137px;background:linear-gradient(180deg,#e8ecec 0%,#d4dedc 45%,#1aa38c 46%,#1aa38c 70%,#e3e8e8 71%)}

/* personnel page */
.ppl-title{left:0;width:310px;top:42px;text-align:center;font-size:7.5px;font-weight:700;color:var(--green)}
.person{position:absolute;left:16px;width:279px}
.p-row{display:flex;height:13px;font-size:6px;font-weight:700;color:var(--white)}
.p-row span{display:flex;align-items:center;padding-left:4px}
.p-key{background:#a3a3a3;justify-content:center;padding-left:0!important}
.p-val{background:var(--green)}
.p-exp{display:flex;height:13px;font-size:4.7px;margin-top:1px}
.p-exp .p-key{width:46px;background:#a3a3a3;color:var(--white);font-weight:600;display:flex;align-items:center}
.p-exp .p-val{flex:1;color:var(--white);font-weight:500;display:flex;align-items:center;padding-left:4px;line-height:1.15}
.p-desc{border:.7px solid var(--green);font-size:4.5px;line-height:1.3;padding:3px 4px;margin-top:1px}

/* back cover */
.back{background:var(--green)}
.back-name{left:0;top:0;width:310px;height:437px;display:flex;align-items:center;justify-content:center}
.back .brand{color:var(--white);font-size:30px}
</style>
</head>
<body>
<main class="sheet-grid">

  <!-- Cover -->
  <section class="page cover">
    <div class="abs cover-top"><span class="brand">VANTAFLO</span></div>
    <div class="photo cover-photo" role="img" aria-label="Dusk photograph of a solar array beside a small onshore gas processing plant"></div>
    <div class="abs cover-band">
      <h1 class="cover-title">CAPABILITY STATEMENT</h1>
      <p class="cover-sub">SIMPLIFY PROJECT EXECUTION,<br>STREAMLINE OPERATIONS</p>
      <p class="cover-url">www.vantaflo.example</p>
    </div>
  </section>

  <!-- Introduction -->
  <section class="page intro">
    <div class="photo intro-photo" role="img" aria-label="Photograph of gas plant pipework, valves and process equipment under blue sky"></div>
    <svg class="abs" style="left:0;top:150px" width="310" height="30"><polygon points="0,30 310,0 310,30" fill="#fff"/></svg>
    <h2 class="abs h-green intro-h">What is a Project Delivery Partner?</h2>
    <p class="abs body intro-p">A Project Delivery Partner (PDP) provides integrated project management along with technical, commercial and delivery support services to help an organisation successfully deliver a project. The PDP acts as the owner's team while the owner retains accountability and key decision-making authority.</p>
    <p class="abs principles-h">PDP Core Principles:</p>
    <ol class="abs principles">
      <li>1.&nbsp;&nbsp;Owner controls the project</li>
      <li>2.&nbsp;&nbsp;PDP enables delivery &amp; provides assurance</li>
      <li>3.&nbsp;&nbsp;Contractors execute the work</li>
    </ol>
    <div class="abs who-box">
      <h3>WHO ARE VANTAFLO?</h3>
      <p>Vantaflo are a highly experienced team of Executive, Project, Construction, Commissioning and Operations specialists who combine deep technical knowledge with proven leadership to deliver unique Project Delivery Partner services to organisations in Australia.</p>
      <p class="vision">Our vision is straightforward:<br>Simplify Project Execution,<br>Streamline Operations.</p>
    </div>
    <p class="abs obj-h">PDP OBJECTIVE:</p>
    <p class="abs body obj-p">Deliver the project safely, on schedule, within budget and ready for operations; providing owner capability throughout the project lifecycle.</p>
    <div class="diag-row" style="top:330px"><div class="diag-label">Owner</div><div class="chip" style="left:93px">Operator XYZ</div></div>
    <div class="diag-row" style="top:356px"><div class="diag-label">Project Delivery Partner</div><div class="chip" style="left:93px">Vantaflo</div></div>
    <div class="diag-row" style="top:383px"><div class="diag-label">Contractors</div><div class="chip" style="left:58px">Engineering</div><div class="chip" style="left:93px">Suppliers</div><div class="chip" style="left:128px">Execution</div></div>
    <svg class="corner" width="50" height="30"><polygon points="0,22 50,8 50,15 0,30" fill="#0f7360"/><polygon points="8,30 50,18 50,30" fill="#0f7360"/></svg>
  </section>

  <!-- Services -->
  <section class="page services">
    <svg class="abs slant" width="310" height="30"><polygon points="0,0 310,0 0,30" fill="#e6e7e9"/></svg>
    <p class="abs svc-title">PDP SERVICES:</p>
    <table class="svc-table">
      <thead><tr><th class="num">#</th><th>FUNCTION</th><th class="c">VANTAFLO SERVICE</th></tr></thead>
      <tbody>
        <tr><td class="num">1</td><td class="fn">Project Management</td><td>Planning, Reporting &amp; Delivery Leadership from Concept to Completion</td></tr>
        <tr><td class="num">2</td><td class="fn">Engineering</td><td>Concept Selection, Design Coordination, Technical Assurance &amp; Value Engineering</td></tr>
        <tr><td class="num">3</td><td class="fn">Procurement</td><td>Contracting Strategy, Tender Process &amp; Supplier / Contractor Management</td></tr>
        <tr><td class="num">4</td><td class="fn">Approvals</td><td>Land Access, Regulator Engagement, Safety Case, Permits &amp; Licenses</td></tr>
        <tr><td class="num">5</td><td class="fn">Cost Control</td><td>Budget Development, Forecasting &amp; Management</td></tr>
        <tr><td class="num">6</td><td class="fn">Scheduling</td><td>Master Schedule Development, WBS, Resource Allocation, Monitoring &amp; Updating</td></tr>
        <tr><td class="num">7</td><td class="fn">Risk Management</td><td>Risk Register, Identification, Mitigation &amp; Reporting</td></tr>
        <tr><td class="num">8</td><td class="fn">Governance</td><td>Risk Register, Identification, Mitigation &amp; Reporting</td></tr>
        <tr><td class="num">9</td><td class="fn">Construction</td><td>Management &amp; Coordination of Contractor Execution Teams</td></tr>
        <tr><td class="num">10</td><td class="fn">Commissioning &amp; Start-up</td><td>Lead Commissioning &amp; Start-up, Completions System, Bring the Facility to Steady-State</td></tr>
        <tr><td class="num">11</td><td class="fn">Operations Readiness</td><td>People &amp; Organisation, Process &amp; Procedures, Systems &amp; Technology</td></tr>
        <tr><td class="num">12</td><td class="fn">Operations &amp; Maintenance</td><td>Monitor &amp; Operate Asset, Minimize Downtime, Lowest Possible OPEX for Owner</td></tr>
      </tbody>
    </table>
    <p class="abs roles-title">PDP ROLES &amp; RESPONSIBILITIES:</p>
    <table class="roles-table">
      <thead><tr><th>OWNER</th><th>VANTAFLO SERVICE</th></tr></thead>
      <tbody>
        <tr><td>Sets Project Objectives</td><td>Develops Delivery Plans</td></tr>
        <tr><td>Approves Major Decisions</td><td>Provides Recommendations</td></tr>
        <tr><td>Holds Project Risk</td><td>Identifies and Manages Risks</td></tr>
        <tr><td>Awards Contracts</td><td>Manages Contractor Interfaces</td></tr>
        <tr><td>Provides Funding</td><td>Monitors Cost and Schedule Performance</td></tr>
      </tbody>
    </table>
    <svg class="corner" width="50" height="30"><polygon points="0,22 50,8 50,15 0,30" fill="#0f7360"/><polygon points="8,30 50,18 50,30" fill="#0f7360"/></svg>
  </section>

  <!-- Benefits & challenges -->
  <section class="page benefits">
    <div class="photo ben-bg" role="img" aria-label="Green-tinted photograph of a gas processing facility skyline"></div>
    <div class="abs ben-panel" style="padding:22px 10px 0 10px">
      <p class="panel-h">PDP<br>BENEFITS:</p>
      <ul class="bullets ben-list" style="margin-top:10px">
        <li>Provides owners with access to experienced project delivery capability</li>
        <li>Improved project controls and governance</li>
        <li>Greater flexibility than traditional EPC delivery</li>
        <li>Enhanced visibility and management of cost, schedule and risk</li>
        <li>Scalable resources aligned with project phases</li>
      </ul>
    </div>
    <div class="abs chal-panel" style="padding:35px 10px 0 10px">
      <p class="panel-h">PDP<br>CHALLENGES:</p>
      <ul class="bullets chal-list" style="margin-top:8px">
        <li>Owner retains significant delivery risk</li>
        <li>Requires clear governance and decision-making processes</li>
        <li>Multiple contractor interfaces require strong coordination</li>
        <li>Success depends on collaborative Owner-PDP relationship</li>
      </ul>
    </div>
    <div class="photo ben-art" role="img" aria-label="Stock graphic of a teal banner reading Benefits with arrows and a quality tag"></div>
  </section>

  <!-- Personnel -->
  <section class="page personnel">
    <svg class="abs slant" width="310" height="30"><polygon points="0,0 310,0 0,30" fill="#e6e7e9"/></svg>
    <p class="abs ppl-title">KEY VANTAFLO PERSONNEL</p>

    <div class="person" style="top:57px">
      <div class="p-row"><span class="p-key" style="width:46px">NAME:</span><span class="p-val" style="width:85px">MARTIN HALE</span><span class="p-key" style="width:42px">ROLE:</span><span class="p-val" style="flex:1">EXECUTIVE DIRECTOR</span></div>
      <div class="p-exp"><span class="p-key">35yrs Exp:</span><span class="p-val">Coralline Energy, Northreach Energy, Delvon Group, Ridgeway Energy</span></div>
      <p class="p-desc">Extensive global energy industry experience, from frontline O&amp;M to the boardroom. Respected 'C Suite' leader with a track record of building high performing teams that deliver outstanding results.</p>
    </div>

    <div class="person" style="top:125px">
      <div class="p-row"><span class="p-key" style="width:46px">NAME:</span><span class="p-val" style="width:85px">GRAHAM TULLOCH</span><span class="p-key" style="width:42px">ROLE:</span><span class="p-val" style="flex:1">TECHNICAL DIRECTOR</span></div>
      <div class="p-exp"><span class="p-key">40yrs Exp:</span><span class="p-val">Harbourline, Tessaro, Meridia Petroleum, Delvon Group, Ridgeway Energy</span></div>
      <p class="p-desc">Senior Logistics &amp; Supply Chain Manager / Procurement Manager with strong operational, commercial, project management, negotiating &amp; relationship building skills. Experienced in operating complex and diverse logistics operations, significantly improving service levels whilst reducing cost.</p>
    </div>

    <div class="person" style="top:199px">
      <div class="p-row"><span class="p-key" style="width:46px">NAME:</span><span class="p-val" style="width:85px">ROWAN PRYCE</span><span class="p-key" style="width:42px">ROLE:</span><span class="p-val" style="flex:1">COMMERCIAL DIRECTOR</span></div>
      <div class="p-exp" style="height:19px"><span class="p-key">39yrs Exp:</span><span class="p-val">Coralline Energy, Northreach Energy, Eastgate Petroleum, Meridia Petroleum, Lantern Gas Group, Kestrel Gas, Delvon Group, Ridgeway Energy</span></div>
      <p class="p-desc">Highly skilled &amp; experienced operations &amp; project management professional with 39 years' experience in the global oil &amp; gas industry delivering multiple projects and establishing best in class operational assets. Deep knowledge of project management, construction, commissioning &amp; start-up including a global functional assurance role.</p>
    </div>

    <div class="person" style="top:287px">
      <div class="p-row"><span class="p-key" style="width:46px">NAME:</span><span class="p-val" style="width:85px">JOEL BARROW</span><span class="p-key" style="width:42px">ROLE:</span><span class="p-val" style="flex:1">OPERATIONS DIRECTOR</span></div>
      <div class="p-exp"><span class="p-key">27yrs Exp:</span><span class="p-val">Meridia Petroleum, Lantern Gas Group, Kestrel Gas, Delvon Group, Ridgeway Energy</span></div>
      <p class="p-desc">27 years' success leading operations, maintenance and commissioning teams on on shore and offshore oil and gas production platforms, FPSOs, gas processing, coal seam gas, refrigeration facilities, and chemical refineries.<br>Results driven and enthusiastic Leader with a proven track record of delivery.</p>
    </div>
    <svg class="corner" width="50" height="30"><polygon points="0,22 50,8 50,15 0,30" fill="#0f7360"/><polygon points="8,30 50,18 50,30" fill="#0f7360"/></svg>
  </section>

  <!-- Back cover -->
  <section class="page back">
    <div class="abs back-name"><span class="brand">VANTAFLO</span></div>
  </section>

</main>
</body>
</html>
```